Website for Torvel Capital - investment banking firm

We have a corporate identity (thanks to Ranjita/41238) and want to extend that into a website design.  See the attached zipped files.
We have software folks in-house to do the coding.
See the attached Project Brief & Notes for more details.  Don't worry about the actual text - lorem ipsum will be fine.
The server will be Apache.
Thank you!
Desmond

```html
<!DOCTYPE html>
<html lang="en">
<head>
<meta charset="utf-8">
<title>Torvel Capital</title>
<link rel="stylesheet" href="https://fonts.googleapis.com/css2?family=Open+Sans:wght@300;400;600&family=Raleway:wght@400;700&display=swap">
<style>
:root{
  --bar:#1b1b1b;
  --panel:#1d1d1d;
  --panel-dark:#0d0d0d;
  --page:#86869a;
  --footer:#1f1f1f;
  --bottom:#0e0e0e;
  --text:#ffffff;
  --muted:#9a9a9a;
  --rule:#4a4a4a;
  --blue:#1f4f9c;
  --brand:#1d3f7a;
}
*{margin:0;padding:0;box-sizing:border-box}
html,body{width:1152px;height:1200px;overflow:hidden}
body{position:relative;background:var(--page);font-family:"Open Sans",Arial,sans-serif;color:var(--text)}
.abs{position:absolute}
ul{list-style:none}

.topbar{left:0;top:0;width:1152px;height:38px;background:var(--bar);font-size:12px}
.topbar .region{left:106px;top:10px;display:flex;align-items:center;gap:10px}
.topbar .sep{margin:0 4px}
.topbar .phone{right:106px;top:11px;display:flex;align-items:center;gap:7px}

.hero{left:0;top:38px;width:1152px;height:428px;
  background:linear-gradient(90deg,#4f4f5a 0%,#2a2d38 25%,#8fa7c9 40%,#3a3c46 55%,#6a6a72 75%,#c8a86a 88%,#8a8896 100%)}
.hero-fade{left:0;top:370px;width:1152px;height:96px;background:linear-gradient(180deg,rgba(160,130,80,0),rgba(190,160,110,.55))}

.sidebar{left:106px;top:38px;width:209px;height:370px;background:linear-gradient(180deg,#262626,#0f0f0f)}
.brand{left:0;top:0;width:209px;height:111px;background:#fff;display:flex;align-items:center;justify-content:center;gap:8px}
.brand .mark{width:26px;height:26px;border-radius:50%;background:var(--brand)}
.brand .name{font-family:"Open Sans",sans-serif;font-size:18px;font-weight:400;color:var(--brand)}
.nav{left:13px;top:127px;width:180px;font-size:12px}
.nav li{height:29px;line-height:29px;border-bottom:1px solid var(--rule);padding-left:0}
.search{left:13px;top:290px;width:181px;height:25px;border-radius:3px;background:linear-gradient(#f2f2f2,#d6d6d6);font-size:9px;color:#bbb;padding:6px 9px}
.search svg{position:absolute;right:9px;top:6px}

.caption{left:315px;top:259px;width:419px;height:149px;background:rgba(20,20,20,.85)}
.caption h1{position:absolute;left:5px;top:16px;font-family:"Raleway",sans-serif;font-weight:400;font-size:28px;line-height:34px;white-space:nowrap}
.caption h1 b{font-weight:700}
.btn{left:9px;top:97px;width:114px;height:34px;background:var(--blue);font-size:14px;line-height:34px;padding-left:13px}

.box{background:linear-gradient(180deg,#2b2b2b,#0c0c0c)}
.services{left:106px;top:467px;width:610px;height:152px}
.box h2{position:absolute;font-weight:400;font-size:21px}
.services h2{left:16px;top:8px}
.svc{top:47px;width:165px}
.svc .ph{height:60px}
.svc p{margin-top:11px;font-size:15px}
.testimonial{left:731px;top:467px;width:315px;height:152px}
.testimonial h2{left:16px;top:8px}
.testimonial h2 small{font-size:12px;color:#bbb;margin-left:6px}
.testimonial .ph{left:15px;top:47px;width:135px;height:60px;background:linear-gradient(135deg,#e5e8ec,#aab4c2 60%,#6d7888)}
.testimonial .quote{left:163px;top:46px;width:140px;font-size:12px;line-height:19px}
.testimonial .more{left:16px;top:116px;font-size:13px}

.details{left:106px;top:635px;width:940px;height:211px}
.col{top:21px}
.col h3{font-weight:400;font-size:21px;margin-bottom:12px}
.col li{font-size:12.5px;color:var(--muted);height:27px;font-weight:300;white-space:nowrap}
.col li::before{content:"›";margin-right:9px;color:#bbb}
.col li.all{font-size:11.5px;height:20px}
.divider{top:15px;width:1px;height:173px;background:#3f3f3f}

.footer{left:0;top:899px;width:1152px;height:253px;background:var(--footer)}
.footer h4{font-weight:400;font-size:18px;position:absolute;top:27px}
.flist{top:81px;font-size:12px}
.flist li{height:19px}
.flist li::before{content:"•";margin-right:8px}
.contact{left:492px;top:82px;font-size:12px;line-height:20px}
.contact div{display:flex;gap:7px;align-items:flex-start}
.contact svg{margin-top:4px;flex:none}
.map{left:708px;top:73px;width:307px;height:127px;border:2px solid #fff;background:linear-gradient(135deg,#e9e4d6,#f3efe3 50%,#b9cde3)}
.bottom{left:0;top:1152px;width:1152px;height:48px;background:var(--bottom);font-size:13px;text-align:center;line-height:48px}
</style>
</head>
<body>

<header class="abs topbar">
  <div class="abs region">
    <svg width="34" height="18" viewBox="0 0 34 18"><circle cx="12" cy="9" r="8" fill="none" stroke="#fff" stroke-width="1.5"/><path d="M4 9h16M12 1v16M6 4c4 2 8 2 12 0M6 14c4-2 8-2 12 0" stroke="#fff" stroke-width="1" fill="none"/><path d="M27 8l3 3 3-3z" fill="#fff"/></svg>
    <span>Asia</span><span class="sep">|</span><span>Contact us</span>
  </div>
  <div class="abs phone">
    <svg width="14" height="14" viewBox="0 0 14 14"><path d="M3 1l3 3-2 2c1 2 2 3 4 4l2-2 3 3-2 2C6 13 1 8 1 3z" fill="#fff"/></svg>
    <span>0800.418.266</span>
  </div>
</header>

<section class="abs hero" role="img" aria-label="Businessman in a suit stacking rising columns of gold coins"></section>
<div class="abs hero-fade"></div>

<aside class="abs sidebar">
  <div class="abs brand"><span class="mark"></span><span class="name">Torvel Capital</span></div>
  <ul class="abs nav">
    <li>Home</li><li>About</li><li>Services</li><li>Current Engagements</li><li>Completed Transactions</li>
  </ul>
  <div class="abs search">Search...
    <svg width="12" height="12" viewBox="0 0 12 12"><circle cx="5" cy="5" r="3.8" fill="none" stroke="#999" stroke-width="1.4"/><path d="M8 8l3 3" stroke="#999" stroke-width="1.6"/></svg>
  </div>
</aside>

<div class="abs caption">
  <h1>Torvel Capital, <b>LLC Investment</b><br>Banking Mergers &amp;Acquisitions</h1>
  <div class="abs btn">Read More &nbsp;››</div>
</div>

<section class="abs box services">
  <h2>Our services</h2>
  <div class="abs svc" style="left:18px"><div class="ph" role="img" aria-label="Hand placing coins on a stack over financial charts" style="background:linear-gradient(135deg,#8fd0dc,#c9b88a)"></div><p>Buy-SideAcquisitions</p></div>
  <div class="abs svc" style="left:226px"><div class="ph" role="img" aria-label="Hand holding a bank card over a laptop keyboard" style="background:linear-gradient(135deg,#2d3442,#8fa6c4 60%,#dfe6ee)"></div><p>Recapitalizations</p></div>
  <div class="abs svc" style="left:429px"><div class="ph" role="img" aria-label="Globe resting on banknotes" style="background:linear-gradient(135deg,#d8dee8,#6f8fbf 70%,#2b4f8a)"></div><p>Sell-SideTransactions</p></div>
</section>

<section class="abs box testimonial">
  <h2>Testimonial<small>Lena Morrow</small></h2>
  <div class="abs ph" role="img" aria-label="Business team in a bright office"></div>
  <p class="abs quote">Lorem ipsum dolor sit amet, consectetur adipisicing elit.</p>
  <div class="abs more">Read more &nbsp;››</div>
</section>

<section class="abs box details">
  <div class="abs col" style="left:19px"><h3>Buy-SideAcquisitions</h3><ul>
    <li>Lorem ipsum dolor sit amet, consectetur</li><li>adipisicing elit, sed do eiusmod tempor</li><li>incididunt ut labore et dolore magna aliqua.</li><li>Ut enim ad minim veniam</li><li class="all">Veiw all</li></ul></div>
  <div class="abs divider" style="left:311px"></div>
  <div class="abs col" style="left:338px"><h3>Recapitalizations</h3><ul>
    <li>Lorem ipsum dolor sit amet, consectetur</li><li>adipisicing elit, sed do eiusmod tempor</li><li>incididunt ut labore et dolore magna aliqua.</li><li>Ut enim ad minim veniam</li><li class="all">Veiw all</li></ul></div>
  <div class="abs divider" style="left:628px"></div>
  <div class="abs col" style="left:663px"><h3>Sell-SideTransactions</h3><ul>
    <li>Lorem ipsum dolor sit amet, consectetur</li><li>adipisicing elit, sed do eiusmod tempor</li><li>incididunt ut labore et dolore magna aliqua.</li><li>Ut enim ad minim veniam</li><li class="all">Veiw all</li></ul></div>
</section>

<footer class="abs footer">
  <h4 style="left:108px">Site Linke</h4>
  <h4 style="left:330px">Resources</h4>
  <h4 style="left:492px">Contact us</h4>
  <h4 style="left:706px">Our Location</h4>
  <ul class="abs flist" style="left:108px">
    <li>Home</li><li>About</li><li>Services</li><li>Current Engagements</li><li>Completed Transactions</li>
  </ul>
  <ul class="abs flist" style="left:332px;top:83px">
    <li>Blog</li><li>Articles</li><li>Webinars</li><li>Events</li><li>Downloads</li>
  </ul>
  <div class="abs contact">
    <div><svg width="13" height="11" viewBox="0 0 13 11"><path d="M6.5 0L0 5.5h2V11h3.5V7.5h2V11H11V5.5h2z" fill="#ddd"/></svg><span>Request A Free Demo<br>Contact</span></div>
    <div><svg width="13" height="12" viewBox="0 0 13 12"><rect x="3" y="0" width="6" height="11" rx="1" fill="none" stroke="#ddd" stroke-width="1.3"/></svg><span>Phone: 866-540-3192</span></div>
    <div><svg width="13" height="12" viewBox="0 0 13 12"><rect x="0" y="3" width="13" height="8" fill="#ddd"/><rect x="3" y="0" width="7" height="4" fill="#ddd"/><rect x="3" y="6" width="7" height="3" fill="#1f1f1f"/></svg><span>Fax: 866-540-3198</span></div>
  </div>
  <div class="abs map" role="img" aria-label="Road map of the region with office location pins"></div>
</footer>

<div class="abs bottom">© Copyright 2014. All rights reserved.</div>

</body>
</html>
```